Clear Coat 5L & 2.5L kit

Clear coat 5 Liter with 2.5 Liter hardener
I attached few examples
Required size:
5L
Actual size is: 22.875 x 10.4375 inch
With bleed added: 23.125 x 10.6875 inch
2.5L
Actual size is: 22.875 x 6.1875 inch
With bleed added: 23.125x6.2125 inch

Thanks

```html
<!DOCTYPE html>
<html lang="en">
<head>
<meta charset="utf-8">
<title>Alto Refinish – Prima Clear Coat Kit Labels</title>
<link rel="stylesheet" href="https://fonts.googleapis.com/css2?family=Montserrat:wght@600;700;800&display=swap">
<style>
  :root {
    --page-bg: #f5f5f7;
    --label-dark: #333233;
    --label-red: #e2343a;
    --brand-yellow: #f7d21e;
    --ink-dark: #2f2c2b;
    --text-light: #ffffff;
    --gold-edge: #d9a46a;
  }
  html, body {
    margin: 0;
    padding: 0;
    width: 1200px;
    height: 1118px;
    overflow: hidden;
    background: var(--page-bg);
    font-family: "Montserrat", sans-serif;
  }
  .label-set {
    position: relative;
    width: 1200px;
    height: 1118px;
  }
  .label { position: absolute; display: block; }
  .label--5l { left: 221px; top: 167px; width: 458px; height: 818px; }
  .label--25l { left: 723px; top: 415px; width: 320px; height: 576px; }
  .brand-name { fill: var(--brand-yellow); font-weight: 800; }
  .product-name { fill: var(--ink-dark); font-weight: 800; }
  .product-type { fill: var(--ink-dark); font-weight: 700; }
  .spec-text { fill: var(--ink-dark); font-weight: 800; }
  .feature-text { fill: var(--ink-dark); font-weight: 600; }
  .volume-text { fill: var(--text-light); font-weight: 800; }
  .spec-box { fill: none; stroke: var(--ink-dark); stroke-width: 2; }
  .spec-divider { stroke: var(--ink-dark); stroke-width: 2; }
</style>
</head>
<body>
<main class="label-set">

  <!-- 5 litre clear coat label -->
  <svg class="label label--5l" viewBox="275 208 568 1014" xmlns="http://www.w3.org/2000/svg" aria-label="Prima Clear Coat 5L label">
    <defs>
      <linearGradient id="gold-large" x1="0" y1="0" x2="1" y2="0">
        <stop offset="0" stop-color="#c98f55"/>
        <stop offset="0.25" stop-color="#f8d2a2"/>
        <stop offset="0.6" stop-color="#dcaa73"/>
        <stop offset="1" stop-color="#b5743a"/>
      </linearGradient>
    </defs>
    <rect x="275" y="208" width="568" height="1014" fill="url(#gold-large)"/>
    <rect x="275" y="208" width="568" height="660" fill="var(--label-dark)"/>
    <rect x="275" y="215" width="568" height="40" fill="var(--label-red)"/>
    <rect x="275" y="255" width="568" height="3" fill="var(--gold-edge)"/>
    <path d="M275 630 Q560 585 843 695 L843 1130 L275 1130 Z" fill="url(#gold-large)"/>
    <path d="M275 610 Q545 572 843 682 L843 692 Q545 588 275 624 Z" fill="var(--label-red)"/>

    <text class="brand-name" x="420" y="466" font-size="86">ALTO</text>
    <text class="brand-name" x="420" y="520" font-size="52" letter-spacing="8">REFINISH</text>

    <text class="product-name" x="560" y="778" font-size="88" text-anchor="middle" letter-spacing="12">PRIMA</text>
    <text class="product-type" x="560" y="824" font-size="35" text-anchor="middle">CLEAR COAT</text>

    <rect class="spec-box" x="420" y="862" width="282" height="60"/>
    <line class="spec-divider" x1="562" y1="862" x2="562" y2="922"/>
    <text class="spec-text" x="491" y="904" font-size="28" text-anchor="middle">2:1 MIX</text>
    <text class="spec-text" x="632" y="904" font-size="28" text-anchor="middle">2.1 VOC</text>

    <text class="feature-text" x="555" y="1009" font-size="28" text-anchor="middle">HIGH GLOSS</text>
    <text class="feature-text" x="555" y="1043" font-size="28" text-anchor="middle">GOOD LEVELING</text>
    <text class="feature-text" x="555" y="1077" font-size="28" text-anchor="middle">EASY APPLICATION</text>

    <rect x="275" y="1130" width="568" height="62" fill="var(--label-dark)"/>
    <text class="volume-text" x="545" y="1175" font-size="40" text-anchor="middle">5L</text>
  </svg>

  <!-- 2.5 litre hardener label -->
  <svg class="label label--25l" viewBox="898 515 397 715" xmlns="http://www.w3.org/2000/svg" aria-label="Prima Hardener 2.5L label">
    <defs>
      <linearGradient id="gold-small" x1="0" y1="0" x2="1" y2="0">
        <stop offset="0" stop-color="#c98f55"/>
        <stop offset="0.25" stop-color="#f8d2a2"/>
        <stop offset="0.6" stop-color="#dcaa73"/>
        <stop offset="1" stop-color="#b5743a"/>
      </linearGradient>
    </defs>
    <rect x="898" y="515" width="397" height="715" fill="url(#gold-small)"/>
    <rect x="898" y="515" width="397" height="345" fill="var(--label-dark)"/>
    <rect x="898" y="518" width="397" height="30" fill="var(--label-red)"/>
    <rect x="898" y="548" width="397" height="2" fill="var(--gold-edge)"/>
    <path d="M898 808 Q1100 780 1295 857 L1295 1160 L898 1160 Z" fill="url(#gold-small)"/>
    <path d="M898 795 Q1095 768 1295 847 L1295 855 Q1095 781 898 806 Z" fill="var(--label-red)"/>

    <text class="brand-name" x="1000" y="693" font-size="56">ALTO</text>
    <text class="brand-name" x="1000" y="732" font-size="34" letter-spacing="5">REFINISH</text>

    <text class="product-name" x="1097" y="912" font-size="60" text-anchor="middle" letter-spacing="8">PRIMA</text>
    <text class="product-type" x="1097" y="945" font-size="25" text-anchor="middle">HARDENER</text>

    <rect class="spec-box" x="1000" y="972" width="195" height="42"/>
    <line class="spec-divider" x1="1098" y1="972" x2="1098" y2="1014"/>
    <text class="spec-text" x="1049" y="1001" font-size="19" text-anchor="middle">2:1 MIX</text>
    <text class="spec-text" x="1147" y="1001" font-size="19" text-anchor="middle">2.1 VOC</text>

    <text class="feature-text" x="1093" y="1075" font-size="20" text-anchor="middle">HIGH GLOSS</text>
    <text class="feature-text" x="1093" y="1098" font-size="20" text-anchor="middle">GOOD LEVELING</text>
    <text class="feature-text" x="1093" y="1122" font-size="20" text-anchor="middle">EASY APPLICATION</text>

    <rect x="898" y="1160" width="397" height="42" fill="var(--label-dark)"/>
    <text class="volume-text" x="1086" y="1192" font-size="28" text-anchor="middle">2.5L</text>
  </svg>

</main>
</body>
</html>
```